Business Card

Please design a business card with our logo on a cream coloured background and include the following information:

Tallowmere Shopping Centre
ph (08) 9341 7086

sales@velvetpetalblooms.com

www.velvetpetalblooms.com

on reverse:

Find us on Bloomfeed
bloomfeed.net/velvetpetalblooms

```html
<!DOCTYPE html>
<html lang="en">
<head>
<meta charset="utf-8">
<title>Velvet Petal Blooms – Business Card</title>
<link rel="stylesheet" href="https://fonts.googleapis.com/css2?family=Cabin:wght@400;500&family=Cabin+Condensed:wght@600&display=swap">
<style>
  :root {
    --cream: #efecc3;
    --leaf: #547a1e;
    --ink: #383838;
    --sheet: #ffffff;
  }
  html, body {
    margin: 0;
    padding: 0;
    overflow: hidden;
    background: var(--sheet);
  }
  .sheet {
    position: relative;
    width: 871px;
    height: 1200px;
    overflow: hidden;
    background: var(--sheet);
    font-family: "Cabin", sans-serif;
    color: var(--ink);
  }
  .card {
    position: absolute;
    left: 0;
    width: 871px;
    background: var(--cream);
  }
  .card--reverse { top: 0; height: 565px; }
  .card--front { top: 634px; height: 566px; }

  .brand-dot {
    position: absolute;
    border-radius: 50%;
    background: var(--leaf);
  }

  /* Reverse side */
  .card--reverse .brand-dot {
    left: 361px; top: 60px; width: 150px; height: 150px;
  }
  .card--reverse .brand-name {
    position: absolute;
    left: 0; right: 0; top: 250px;
    margin: 0;
    text-align: center;
    font-family: "Cabin Condensed", sans-serif;
    font-size: 64px;
    font-weight: 600;
    line-height: 1.2;
    color: var(--leaf);
  }
  .social-link {
    position: absolute;
    left: 0; right: 0; top: 449px;
    margin: 0;
    text-align: center;
    font-size: 23px;
    line-height: 1.2;
    letter-spacing: 0.9px;
  }

  /* Front side */
  .card--front .brand-dot {
    left: 187px; top: 42px; width: 124px; height: 124px;
  }
  .card--front .brand-name {
    position: absolute;
    left: 35px; top: 170px;
    margin: 0;
    font-family: "Cabin Condensed", sans-serif;
    font-size: 54px;
    font-weight: 600;
    line-height: 1.2;
    color: var(--ink);
  }
  .contact {
    position: absolute;
    left: 38px;
    margin: 0;
    font-size: 20px;
    line-height: 1.2;
    letter-spacing: 0.8px;
  }
  .contact--address { top: 287px; font-size: 25px; letter-spacing: 0.9px; }
  .contact--phone { top: 320px; font-size: 21px; }
  .contact--email { top: 389px; }
  .contact--web { top: 478px; }

  .crop-marks {
    position: absolute;
    inset: 0;
    pointer-events: none;
  }
</style>
</head>
<body>
<main class="sheet">
  <section class="card card--reverse">
    <span class="brand-dot"></span>
    <h2 class="brand-name">Velvet Petal Blooms</h2>
    <p class="social-link">bloomfeed.net/velvetpetalblooms</p>
  </section>

  <section class="card card--front">
    <span class="brand-dot"></span>
    <h1 class="brand-name">Velvet Petal Blooms</h1>
    <p class="contact contact--address">Tallowmere Shopping Centre</p>
    <p class="contact contact--phone">ph (08) 9341 7086</p>
    <p class="contact contact--email">sales@velvetpetalblooms.com</p>
    <p class="contact contact--web">www.velvetpetalblooms.com</p>
  </section>

  <svg class="crop-marks" width="871" height="1200" viewBox="0 0 871 1200" aria-hidden="true">
    <g stroke="#555" stroke-width="1" fill="none">
      <path d="M0 15.5 H9 M15.5 0 V9 M871 15.5 H862 M855.5 0 V9"/>
      <path d="M0 549.5 H9 M15.5 556 V565 M871 549.5 H862 M855.5 556 V565"/>
      <path d="M0 649.5 H9 M15.5 634 V643 M871 649.5 H862 M855.5 634 V643"/>
      <path d="M0 1184.5 H9 M15.5 1191 V1200 M871 1184.5 H862 M855.5 1191 V1200"/>
    </g>
  </svg>
</main>
</body>
</html>
```